Business cards for Paperleaf Sprites

Please note that the color of the logo has been changed from green to teal blue. Sorry for the changing!

Anything will go but want to have some funky side.

I would like the front of the business card is the logo and business information and the back side is the Adult Coloring, so that would attract the customer to do the coloring on the other side. Have more interactive side. (pictures for references only can see it below). Fairies on the back of the card for coloring and whatever you want to adds on to color, like flowers, nature etc......

Scrapbooking is not just paper, it also involves watercolor, mixed media, art, all the fun stuff.

Another keypoint I would like to stress on is the back of the business card should be Adult Coloring and make sure you are not google and use the search engine to copy and paste because of the copyright issue.

As a designer, I am sure you all can create beautiful artwork.

Please submit your creativities!

Want the business card is out of the ordinary and customers would like to keep that as a keepsake rather than treat like a regular business card and trash it. Fonts cannot be too small, consider some of the customers have to wear bi-focal eyeglasses.

Thanks a lot!

Target Market(s)

Scrapbooking, Card making, papercraft, stampin‘ , gifts items , etc.

Industry/Entity Type

Retail

Contact Information for Business Card

Color Scheme, please match with the Logo. Watercolor effect is nice!
Thanks!

Font styles to use
Serif

Requirements
Must have
• I would like Elegant and playful.
• Thanks!
Nice to have
• Watercolor effect or check out the Adult Coloring Book, I am thinking we can use a double-sided business card, one side for the information and the other side for people can do the coloring. I have attached 2 pictures for reference.
Should not have
• No black color on the background please!

```html
<!DOCTYPE html>
<html lang="en">
<head>
<meta charset="utf-8">
<title>Paperleaf Sprites — Stationery Set</title>
<link href="https://fonts.googleapis.com/css2?family=Amatic+SC:wght@700&display=swap" rel="stylesheet">
<style>
  :root {
    --bg-navy: #0c2c41;
    --ink-navy: #12324a;
    --paper: #f7f7f6;
    --paper-shade: #e9e9e8;
    --teal: #2ab4c0;
    --coral: #e9585c;
    --cream: #efe9dc;
  }
  html, body {
    margin: 0;
    padding: 0;
    width: 1200px;
    height: 1200px;
    overflow: hidden;
    background: var(--bg-navy);
  }
  .canvas {
    position: relative;
    width: 1200px;
    height: 1200px;
    background: var(--bg-navy);
    font-family: "Amatic SC", "Arial Narrow", sans-serif;
    font-weight: 700;
    color: var(--ink-navy);
  }
  .piece {
    position: absolute;
    overflow: hidden;
    background: linear-gradient(135deg, var(--paper) 0%, #ffffff 35%, var(--paper-shade) 60%, #ffffff 85%, var(--paper) 100%);
  }
  .piece svg.pattern {
    position: absolute;
    left: 0;
    top: 0;
  }
  .banner { left: 143px; top: 114px; width: 912px; height: 143px; }
  .tall-card { left: 143px; top: 318px; width: 384px; height: 792px; }
  .card-info { left: 587px; top: 318px; width: 468px; height: 254px; }
  .card-center { left: 587px; top: 587px; width: 468px; height: 253px; }
  .card-back { left: 587px; top: 855px; width: 468px; height: 255px; }

  .brand {
    position: absolute;
    margin: 0;
    font-size: 42px;
    font-weight: 700;
    color: var(--ink-navy);
    line-height: 38px;
    letter-spacing: 1px;
    text-transform: uppercase;
    white-space: nowrap;
  }
  .brand span { display: block; }
  .banner .brand { left: 562px; top: 32px; width: 240px; text-align: center; }
  .tall-card .brand { left: 0; width: 384px; top: 690px; text-align: center; }
  .card-info .brand { left: 37px; top: 36px; }
  .card-center .brand { left: 110px; width: 248px; top: 28px; text-align: center; }

  .contact {
    position: absolute;
    margin: 0;
    color: var(--ink-navy);
    text-transform: uppercase;
    white-space: nowrap;
  }
  .contact .name { font-size: 24px; line-height: 28px; letter-spacing: 0.5px; margin-bottom: 4px; }
  .contact .line { font-size: 16px; line-height: 21px; }
  .card-info .contact { left: 37px; top: 134px; }
  .card-center .contact { left: 110px; width: 248px; top: 134px; text-align: center; }
</style>
</head>
<body>
<svg width="0" height="0" style="position:absolute" aria-hidden="true">
  <defs>
    <radialGradient id="mandalaTone" cx="50%" cy="50%" r="50%">
      <stop offset="0%" stop-color="#e9585c"/>
      <stop offset="35%" stop-color="#efe9dc"/>
      <stop offset="60%" stop-color="#2ab4c0"/>
      <stop offset="80%" stop-color="#e9585c"/>
      <stop offset="100%" stop-color="#2ab4c0"/>
    </radialGradient>
    <radialGradient id="colouringTone" cx="50%" cy="100%" r="90%">
      <stop offset="0%" stop-color="#f6dcd8"/>
      <stop offset="45%" stop-color="#f4efe4"/>
      <stop offset="100%" stop-color="#d9eff1"/>
    </radialGradient>
  </defs>
</svg>

<main class="canvas">
  <section class="piece banner">
    <svg class="pattern" width="912" height="143" viewBox="0 0 912 143" role="img" aria-label="Teal and coral mandala ornament band">
      <path d="M0 0 H520 Q545 30 535 70 Q545 110 520 143 H0 Z" fill="url(#mandalaTone)"/>
    </svg>
    <h2 class="brand"><span>Paperleaf</span><span>Sprites</span></h2>
  </section>

  <section class="piece tall-card">
    <svg class="pattern" width="384" height="792" viewBox="0 0 384 792" role="img" aria-label="Half mandala ornament in teal, coral and cream">
      <circle cx="0" cy="325" r="322" fill="url(#mandalaTone)"/>
    </svg>
    <h2 class="brand"><span>Paperleaf</span><span>Sprites</span></h2>
  </section>

  <section class="piece card-info">
    <svg class="pattern" width="468" height="254" viewBox="0 0 468 254" role="img" aria-label="Corner mandala ornament in teal, coral and cream">
      <circle cx="480" cy="250" r="255" fill="url(#mandalaTone)"/>
    </svg>
    <h2 class="brand"><span>Paperleaf</span><span>Sprites</span></h2>
    <div class="contact">
      <div class="name">Your Name</div>
      <div class="line">Phone: +1234567890</div>
      <div class="line">Adress: Country, City, Adress</div>
      <div class="line">E-mail: mail@mail.com</div>
    </div>
  </section>

  <section class="piece card-center">
    <svg class="pattern" width="468" height="253" viewBox="0 0 468 253" role="img" aria-label="Two half mandala ornaments framing the card edges">
      <circle cx="0" cy="126" r="122" fill="url(#mandalaTone)"/>
      <circle cx="468" cy="126" r="122" fill="url(#mandalaTone)"/>
    </svg>
    <h2 class="brand"><span>Paperleaf</span><span>Sprites</span></h2>
    <div class="contact">
      <div class="name">Your Name</div>
      <div class="line">Phone: +1234567890</div>
      <div class="line">Adress: Country, City, Adress</div>
      <div class="line">E-mail: mail@mail.com</div>
    </div>
  </section>

  <section class="piece card-back">
    <svg class="pattern" width="468" height="255" viewBox="0 0 468 255" role="img" aria-label="Card back: adult colouring line art of fairies, flowers and mandala motifs, left uncoloured for the customer to fill in">
      <rect width="468" height="255" fill="url(#colouringTone)"/>
      <rect x="10" y="10" width="448" height="235" fill="none" stroke="#12324a" stroke-width="1.5" stroke-dasharray="6 5"/>
    </svg>
  </section>
</main>
</body>
</html>
```